Flyer needed to promote gutter clearance service for established gardening company

We need a bright and engaging flyer to be designed to advertise our gutter clearance service.
Whilst we are a gardening company that normally does more horticultural work, during the winter we offer other services such as gutter clearance where we remove the debris from gutters and thereby reducing the risk of clogs, leakage, breakage and potential structural damage to the property.

Full details of our service, together with our overall brand and colours can be seen on www.marlowtreecare.co.uk/gutters.

We would like you to use the page on the website as a basis to create the flyer and so please feel free to use as much or as little of the wording contained within the webpage on the flyer drawing particular attention to "Prices starting at just £60 for an average 3 bed house". I will upload pictures but please feel free to use other graphics and fonts to make it stand out.

The contact details which should be included within the flyer are as follows:

Marlow Treecare Services Ltd
Orbit Trading Centre
Fairbrook Vale Ind Estate
Swindon
SN4 7HW

Tel: 01793 418302
www.marlowtreecare.co.uk
dean@marlowtreecare.co.uk

The flyers will eventually be printed out in A5 (210mm x 148mm) using Printelle and so needs to be in that size and suitable file for upload.

I have only put this as a 2 day project as its really urgent and I'm hoping we get some great designs in that time.

Target Market(s)

Homeowners between 25 - 65+

Industry/Entity Type

Home Improvement

Font styles to use
Serif
Sans Serif
Decorative
Script

Colors
6b449b
9bcb3c

Requirements
Must have
• Our colours are purple and green as seen on our website www.marlowtreecare.co.uk/gutters. Please use those colours.
• The flyer should draw attention to the following facts:
• We are Marlow Treecare Services Ltd (see attached logo)
• We are offering a Gutter Clearance Service in Swindon
• Prices start at just £60 for the average 3 bed house.
• We are fully insured.
• Our contact details must be included (as in the product description above)
• I have attached pictures but feel free to add other graphics or use fonts to make the flyer more engaging and interesting.
• Additional wording may be taken from the website at the address shown above. You can use as much or as little wording as you like just as long as the message gets across and the flyer contains our contact information and logo and the details shown above.
Nice to have
• I would like a bright and modern design which isn't too busy or cluttered. It should be something that is quick and easy to read.
Should not have
• I don't want it to look too busy or crowded with small type which people just won't read. Whilst I've said you can take whatever wording you want from our website, I'd suggest you don't take it all or too much. I want the main message (as detailed above in 'must haves') to stand out rather than have it contained deep within lots of small type face.

```html
<!DOCTYPE html>
<html lang="en">
<head>
<meta charset="utf-8">
<title>Marlow Treecare – Gutter Clearance Flyer</title>
<link rel="stylesheet" href="https://fonts.googleapis.com/css2?family=Open+Sans:wght@600&family=Cabin:wght@600&family=Bubblegum+Sans&family=Great+Vibes&family=Anton&family=Kaushan+Script&family=Cherry+Swash:wght@700&family=Archivo+Black&display=swap">
<style>
  :root {
    --white: #ffffff;
    --purple-bg: #5236f0;
    --purple-box: #6a12e2;
    --purple-deep: #6b449b;
    --phone-purple: #7a2cf0;
    --green: #6aeb24;
    --green-soft: #9bcb3c;
    --brand-brown: #3b2414;
    --yellow: #efe23a;
  }
  * { margin: 0; padding: 0; box-sizing: border-box; }
  html, body { width: 856px; height: 1200px; overflow: hidden; background: var(--white); }
  .flyer { position: relative; width: 856px; height: 1200px; overflow: hidden; background: var(--white); }
  .shapes { position: absolute; inset: 0; }
  .brand { position: absolute; left: 40px; top: 92px; display: flex; align-items: center; gap: 14px; }
  .brand-dot { width: 34px; height: 34px; border-radius: 50%; background: var(--green-soft); }
  .brand-name { font-family: 'Open Sans', sans-serif; font-weight: 600; font-size: 40px; color: var(--brand-brown); line-height: 1; }
  .question { position: absolute; left: 38px; top: 302px; width: 240px; font-family: 'Open Sans', sans-serif; font-weight: 600; font-size: 50px; line-height: 57px; color: var(--white); }
  .price { position: absolute; left: 420px; top: 264px; width: 304px; height: 304px; text-align: center; color: var(--white); }
  .price-from { position: absolute; left: 40px; top: 32px; width: 240px; font-family: 'Great Vibes', cursive; font-size: 38px; transform: rotate(-10deg); }
  .price-just { position: absolute; left: 0; top: 74px; width: 304px; font-family: 'Great Vibes', cursive; font-size: 62px; }
  .price-amount { position: absolute; left: 0; top: 146px; width: 300px; font-family: 'Anton', sans-serif; font-size: 104px; line-height: 1; }
  .price-note { position: absolute; left: 694px; top: 490px; font-family: 'Great Vibes', cursive; font-size: 40px; line-height: 40px; color: var(--green); font-weight: 700; white-space: nowrap; }
  .intro { position: absolute; font-family: 'Cabin', sans-serif; font-weight: 600; font-size: 31px; color: var(--white); white-space: nowrap; }
  .intro-1 { left: 56px; top: 598px; }
  .intro-2 { left: 172px; top: 654px; }
  .intro-3 { left: 371px; top: 710px; }
  .contact { position: absolute; left: 29px; top: 758px; font-family: 'Bubblegum Sans', sans-serif; color: var(--green); }
  .contact-company { font-size: 33px; line-height: 40px; margin-bottom: 10px; }
  .contact-line { font-size: 27px; line-height: 41px; }
  .insured { position: absolute; left: 60px; top: 1020px; font-family: 'Cherry Swash', serif; font-weight: 700; font-size: 50px; color: var(--green); letter-spacing: 1px; }
  .call-now { position: absolute; left: 640px; top: 986px; width: 190px; font-family: 'Kaushan Script', cursive; font-size: 46px; line-height: 46px; color: var(--phone-purple); transform: rotate(-6deg); }
  .call-now span { display: block; padding-left: 34px; }
  .phone { position: absolute; left: 180px; top: 1090px; font-family: 'Archivo Black', sans-serif; font-size: 78px; font-style: italic; color: var(--phone-purple); -webkit-text-stroke: 2px #b59cf7; letter-spacing: 1px; white-space: nowrap; }
  .email { position: absolute; left: 421px; top: 1168px; font-family: 'Cabin', sans-serif; font-weight: 600; font-size: 25px; color: #c6b2f8; }
</style>
</head>
<body>
<main class="flyer">
  <svg class="shapes" width="856" height="1200" viewBox="0 0 856 1200" aria-hidden="false">
    <defs>
      <linearGradient id="photoTones" x1="0" y1="0" x2="1" y2="1">
        <stop offset="0" stop-color="#8fae4a"/>
        <stop offset="0.45" stop-color="#6d6f6c"/>
        <stop offset="0.75" stop-color="#c98a3e"/>
        <stop offset="1" stop-color="#5e6b62"/>
      </linearGradient>
    </defs>
    <!-- purple main panel -->
    <rect class="panel-main" x="16" y="436" width="840" height="652" fill="var(--purple-bg)"/>
    <rect class="strip-left" x="0" y="560" width="16" height="528" fill="var(--green)"/>
    <!-- green connector band -->
    <rect class="band-green" x="288" y="316" width="170" height="120" fill="var(--green)"/>
    <!-- photo area -->
    <path class="photo-frame" d="M372 0 H856 V488 C760 500 700 470 640 420 C520 330 400 220 372 0 Z" fill="var(--green)"/>
    <path class="photo" role="img" aria-label="Photo of gloved hands clearing autumn leaves from a roof gutter" d="M380 0 H856 V480 C760 490 702 462 644 412 C528 320 410 214 380 0 Z" fill="url(#photoTones)"/>
    <!-- curved arrow -->
    <path class="arrow" d="M270 420 C250 300 330 220 440 205" fill="none" stroke="var(--green)" stroke-width="14"/>
    <path class="arrow-head" d="M430 172 L476 204 L436 240 Z" fill="var(--green)"/>
    <!-- question box -->
    <rect class="question-frame" x="0" y="284" width="296" height="280" rx="44" fill="var(--green)"/>
    <rect class="question-box" x="10" y="296" width="274" height="260" rx="40" fill="var(--purple-box)"/>
    <!-- price circle -->
    <circle class="price-ring" cx="572" cy="416" r="156" fill="var(--green)"/>
    <circle class="price-disc" cx="572" cy="416" r="146" fill="var(--purple-bg)"/>
    <!-- bottom band -->
    <rect class="band-bottom" x="0" y="1088" width="856" height="112" fill="var(--green)"/>
    <rect class="band-bottom-edge" x="0" y="1088" width="16" height="112" fill="var(--purple-box)"/>
    <!-- call bubble -->
    <ellipse class="call-bubble" cx="732" cy="1040" rx="110" ry="62" transform="rotate(-12 732 1040)" fill="var(--yellow)"/>
  </svg>

  <div class="brand">
    <span class="brand-dot"></span>
    <span class="brand-name">Marlow Treecare</span>
  </div>

  <h1 class="question">Have a Dirty, Clogged Gutter?</h1>

  <div class="price">
    <div class="price-from">Starting From</div>
    <div class="price-just">Just</div>
    <div class="price-amount">£60</div>
  </div>
  <div class="price-note">an average<br>3 bed house</div>

  <p class="intro intro-1">We are Marlow Treecare Services Ltd</p>
  <p class="intro intro-2">We are offering a Gutter</p>
  <p class="intro intro-3">Clearance Service in&nbsp; Swindon</p>

  <address class="contact" style="font-style:normal">
    <div class="contact-company">Marlow Treecare Services Ltd</div>
    <div class="contact-line">Orbit Trading Centre</div>
    <div class="contact-line">Fairbrook Vale Ind Estate</div>
    <div class="contact-line">Swindon</div>
    <div class="contact-line">SN4 7HW</div>
    <div class="contact-line">www.marlowtreecare.co.uk</div>
  </address>

  <p class="insured">We are fully insured</p>
  <p class="call-now">Call Us<span>Now</span></p>
  <p class="phone">01793 418302</p>
  <p class="email">dean@marlowtreecare.co.uk</p>
</main>
</body>
</html>
```